Verra needs a new design we have an updated logo and want a high qualitative high end feel

feel and aesthetic should be high qualitative like the packaging in a zuvi or the qualatative weight/feel of an zuvi design. modern, elegant bold.probably just the verra logo on the backone vesion could be blue background white letter ... open to ideas
Target Market(s)
legal, insurance , medical, finance rho 740
Industry/Entity Type
Information Technology
Font styles to use
Serif

```html
<!DOCTYPE html>
<html lang="en">
<head>
<meta charset="utf-8">
<title>Verra Managed Services Group – Business Card</title>
<link rel="stylesheet" href="https://fonts.googleapis.com/css2?family=Lato:wght@400;700&family=Roboto+Condensed:wght@400;700&display=swap">
<style>
  :root {
    --stage: #2a2a2a;
    --card-white: #ffffff;
    --brand-navy: #1a5d9c;
    --brand-blue: #1b6aa8;
    --ink: #2f2f2f;
    --rule: #b5b5b5;
    --back-top: #1a5f99;
    --back-bottom: #1697cf;
    --on-blue: #ffffff;
  }
  * { margin: 0; padding: 0; box-sizing: border-box; }
  html, body { width: 1200px; height: 1200px; overflow: hidden; }
  body { background: var(--stage); position: relative; font-family: "Lato", sans-serif; }

  .card { position: absolute; top: 310px; width: 366px; height: 594px; }
  .card--front { left: 233px; background: var(--card-white); }
  .card--back {
    left: 628px; width: 368px;
    background: linear-gradient(175deg, var(--back-top) 0%, #1a78b5 55%, var(--back-bottom) 100%);
  }

  .wordmark {
    font-family: "Lato", sans-serif;
    font-weight: 700;
    font-size: 96px;
    line-height: 1;
    letter-spacing: -1px;
  }
  .tagline {
    font-family: "Roboto Condensed", sans-serif;
    font-weight: 400;
    font-size: 19px;
    letter-spacing: 0.3px;
    white-space: nowrap;
  }

  .card--front .logo { position: absolute; top: 138px; left: 0; width: 100%; text-align: center; }
  .card--front .wordmark { color: var(--brand-navy); }
  .card--front .tagline { color: var(--brand-navy); margin-top: 10px; }

  .contact { position: absolute; top: 358px; left: 0; width: 100%; text-align: center; color: var(--ink); font-size: 17px; line-height: 21.5px; }
  .contact__name { font-family: "Roboto Condensed", sans-serif; font-weight: 700; font-size: 27px; line-height: 28px; color: var(--brand-blue); }
  .contact__title { margin-bottom: 8px; }
  .contact__rule { width: 144px; height: 1px; background: var(--rule); margin: 0 auto 9px; }
  .contact__label { color: var(--brand-navy); }
  .contact__lines { margin-bottom: 9px; }
  .contact__company { color: var(--brand-navy); }

  .card--back .logo { position: absolute; left: 48px; top: 418px; }
  .card--back .wordmark { color: var(--on-blue); }
  .card--back .tagline { color: var(--on-blue); margin-top: 10px; font-size: 19px; }
</style>
</head>
<body>
  <section class="card card--front">
    <div class="logo">
      <div class="wordmark">verra</div>
      <div class="tagline">MANAGED SERVICES GROUP, INC.</div>
    </div>
    <div class="contact">
      <div class="contact__name">MARCUS HALE</div>
      <div class="contact__title">Managing Director</div>
      <div class="contact__rule"></div>
      <div class="contact__lines">
        <div><span class="contact__label">P:</span> (555) 214-7830</div>
        <div><span class="contact__label">E:</span> help@verramsg.com</div>
      </div>
      <div class="contact__rule"></div>
      <div class="contact__company">Verra Managed Services Group, Inc</div>
      <div>482 Alder Row Suite 310</div>
      <div>Easton, ST 40127</div>
    </div>
  </section>

  <section class="card card--back" role="img" aria-label="Blue gradient card back with soft flowing brand curves">
    <div class="logo">
      <div class="wordmark">verra</div>
      <div class="tagline">MANAGED SERVICES GROUP, INC.</div>
    </div>
  </section>
</body>
</html>
```